Wedding on the paradise

We are getting married in Koh Samui Thailand and need booklet/ concertina that contains the invitation, event program (Day 1 Sunset Cocktail Party, Day 2 Wedding Day, Day 4 Sunset Cruise) and information about the island of Koh Samui.

Also looking for the Wedding Day Program, Menu and card containing guest names.

Below is the link to my favorite invitation and would like similar outcome.

http://www.lumeradesigns.com/wedding/couture.php?c=styles&s=destination&p=tova_marsh

We have international guests and therefore require text in Mongolian and English.

Industry/Entity Type

Wedding

Colors
cedeec

```html
<!DOCTYPE html>
<html lang="en">
<head>
<meta charset="utf-8">
<title>Wedding on the Paradise – Concertina Invitation</title>
<link href="https://fonts.googleapis.com/css2?family=Great+Vibes&family=Tinos&display=swap" rel="stylesheet">
<style>
  :root {
    --sky-top: #ffffff;
    --sky-bottom: #cde6f4;
    --ink-deep: #1d4a8a;
    --ink-soft: #8dcbed;
    --fold-line: #9aa3ab;
    --motif: rgba(255,255,255,0.55);
    --motif-blue: rgba(150,205,236,0.55);
  }
  * { margin: 0; padding: 0; box-sizing: border-box; }
  html, body { width: 1200px; height: 423px; overflow: hidden; background: #fff; }
  .concertina {
    position: relative; width: 1200px; height: 423px;
    display: flex;
    background: linear-gradient(to bottom, var(--sky-top) 0%, var(--sky-bottom) 100%);
  }
  .panel {
    position: relative; width: 300px; height: 423px;
    border-right: 1px solid var(--fold-line);
    text-align: center;
    font-family: "Tinos", "Times New Roman", serif;
    color: var(--ink-soft);
  }
  .panel:last-child { border-right: none; }
  .panel > * { position: absolute; left: 0; right: 0; }
  .date { top: 10px; left: auto; right: 14px; font-size: 13px; }
  .script {
    font-family: "Great Vibes", cursive;
    color: var(--ink-deep);
    font-weight: 400;
    line-height: 1;
  }
  .body-copy { font-size: 13px; line-height: 15.5px; }
  .connector { font-size: 13px; }

  .monogram-wreath {
    top: 25px; left: 72px; width: 156px; height: 156px; border-radius: 50%;
    background: radial-gradient(circle, rgba(180,220,243,0.25) 45%, var(--motif-blue) 62%, rgba(180,220,243,0.15) 72%, transparent 74%);
  }
  .welcome-title { top: 205px; font-size: 46px; }
  .welcome-copy { top: 287px; }

  .island-map {
    top: 112px; left: 70px; width: 280px; height: 310px;
    background: radial-gradient(ellipse at 45% 55%, var(--motif) 0%, rgba(255,255,255,0.15) 60%, transparent 72%);
  }
  .arrow-icon { top: 175px; left: -80px; width: 150px; height: 80px; }
  .day-title { top: 40px; font-size: 50px; }
  .join { top: 138px; }
  .bride { top: 165px; font-size: 44px; }
  .and { top: 226px; }
  .groom { top: 245px; font-size: 44px; }
  .celebrate { top: 307px; }
  .ceremony { top: 354px; }

  .cocktail-title { top: 42px; font-size: 48px; line-height: 58px; }
  .palm-trees {
    top: 110px; left: 200px; width: 180px; height: 313px;
    background: radial-gradient(ellipse at 50% 40%, var(--motif) 0%, rgba(255,255,255,0.2) 55%, transparent 72%);
  }
  .cruise-title { top: 40px; font-size: 48px; }
  .cruise-invite { top: 125px; }
  .boat-name { top: 198px; font-size: 44px; }
  .boat-site { top: 251px; font-size: 12px; }
  .details { top: 296px; font-size: 11px; line-height: 14px; }
  .pricing { top: 365px; font-size: 11px; line-height: 14px; }
</style>
</head>
<body>
<main class="concertina">

  <section class="panel panel-welcome">
    <div class="monogram-wreath" role="img" aria-label="Leaf wreath framing the couple's monogram"></div>
    <h1 class="script welcome-title">Welcome</h1>
    <p class="body-copy welcome-copy">Thank you for sharing this<br>special time with us,<br>as we both look forward<br>to a shared future of love, friendship,<br>and the wonderful closeness<br>that is marriage</p>
  </section>

  <section class="panel panel-wedding">
    <div class="island-map" role="img" aria-label="Faint outline map of Koh Samui island"></div>
    <svg class="arrow-icon" viewBox="0 0 150 80" aria-hidden="true">
      <line x1="10" y1="70" x2="140" y2="12" stroke="rgba(255,255,255,0.7)" stroke-width="2"/>
      <polyline points="124,10 140,12 132,26" fill="none" stroke="rgba(255,255,255,0.7)" stroke-width="2"/>
    </svg>
    <p class="date">13 December 2014</p>
    <h2 class="script day-title">Wedding Day</h2>
    <p class="connector join">Join</p>
    <p class="script bride">Saruul</p>
    <p class="connector and">and</p>
    <p class="script groom">Daniel</p>
    <p class="body-copy celebrate">to celebrate their special day on<br>13 December 2014</p>
    <p class="body-copy ceremony">Ceremony starts 4.30<br>Venue : Baan Talay Villa, Koh Samui Thailand</p>
  </section>

  <section class="panel panel-cocktail">
    <div class="palm-trees" role="img" aria-label="Faint silhouette of palm trees"></div>
    <p class="date">14 December 2014</p>
    <h2 class="script cocktail-title">Sunset Cocktail<br>Party</h2>
  </section>

  <section class="panel panel-cruise">
    <p class="date">15 December 2014</p>
    <h2 class="script cruise-title">Sunset Cruise</h2>
    <p class="body-copy cruise-invite">Join us for a post wedding celebration<br>on a Sunset Cruise on the</p>
    <p class="script boat-name">Blue Heron</p>
    <p class="boat-site">www.blueheron-samui.com</p>
    <p class="details">Date: 15 December 2014<br>RSVP: 14 July 2014<br>E: saruul_b@mailbox.com<br>M:0400-1234-56</p>
    <p class="pricing">Price: 1,567 BAHT PP<br>Children: Under the age of 7 - FREE, over 7 - 700 BAHT</p>
  </section>

</main>
</body>
</html>
```